依頼詳細
■商品の特徴
・使用する原材料は「小麦粉・塩・水」のみ。厳選した国産小麦粉をたっぷりの水で捏ね、みずみずしい透明感とツヤのある麺に仕上げました。
・麺の太さは、細すぎず、適度な噛みごたえ、食べ応えが楽しめます。
・油を使っていないシンプルな原材料で安心感も併せて訴求。

■デザインの方向性
・和紙(雲竜またはミルテア)の風合いを生かす
・和モダン、シンプル、品がある、
・素朴で田舎っぽいがお洒落なイメージも想起させる。
・夏、涼しい、冷たい、水、流れ、波紋など、涼感を想起させるイメージ。
・商品名が筆文字の場合は、達筆すぎない、崩れすぎていない、読みやすいこと。

■留意点
・ジジ臭いのはNG(蕎麦やうどんは、とかくジジ臭くなりがちです)

■ 利用用途
・決定したデザインはそうめんの他、冷麦などシリーズ展開します。
記載項目
■パッケージ仕様
・商品名:青葉台の白糸そうめん(仮名)
・フィルム寸法:W230×H275(オモテ面 W100×H275の範囲をデザイン)
・フィルム材質:レーヨン紙(雲竜またはミルテア)
・色数:5色まで(シズルは無し)
希望イメージ
シンプル 複雑
単色 カラフル
暗い 明るい
日常 高級
遊び心 厳粛
未来的 伝統的
女性的 男性的
希望する色
青系、水色系、グレー系、紫系
納品ファイル
• 高解像度JPG (.jpg)
• イラストレーター形式 (.ai)
• フォトショップ形式 (.psd)
補足説明
合成用の画像を用意しましたので、可能であればこの画像に合成してご提案いただけますでしょか?よろしくお願い致します。
■ 選んだ理由

和風、モダンさのバランスが求めていたものに近い気がしました。売り場のイメージにもマッチしていると感じました。色を変えてのシリーズ展開もしやすそうでした。白を生かした涼感も感じました。

■ 提案者全員のお礼・コメント

この度は素敵なデザインのご提案ありがとうございます。こちらのデザインを元に修正もお願いするかと思います。その際はよろしくお願いいたします。
まずは、修正の方向性を私の方で探って見たいので、イラレのデータをいただけますでしょうか?よろしくお願いいたします。

```html
<!DOCTYPE html>
<html lang="ja">
<head>
<meta charset="utf-8">
<title>青葉台の白糸そうめん パッケージ</title>
<link href="https://fonts.googleapis.com/css2?family=Yuji+Syuku&family=Shippori+Mincho:wght@500&display=swap" rel="stylesheet">
<style>
  :root {
    --canvas: #ffffff;
    --paper: #f3f4f6;
    --paper-edge: #e6e8ec;
    --noodle-light: #ece6d6;
    --noodle-mid: #ddd4bf;
    --ink-navy: #1f2f5c;
    --ripple-deep: #2f56b0;
    --ripple-mid: #6d8fd6;
    --ripple-pale: #c9d6f0;
    --frost: rgba(255,255,255,0.85);
  }
  html, body {
    margin: 0;
    width: 677px;
    height: 1200px;
    overflow: hidden;
    background: var(--canvas);
  }
  .canvas {
    position: relative;
    width: 677px;
    height: 1200px;
  }
  .package {
    position: absolute;
    left: 124px;
    top: 22px;
    width: 430px;
    height: 1160px;
    background: linear-gradient(180deg, var(--paper) 0%, #f8f8fa 50%, var(--paper) 100%);
    box-shadow: 0 0 0 1px var(--paper-edge);
    overflow: hidden;
  }
  .noodle-window {
    position: absolute;
    left: 30px;
    right: 30px;
    top: 120px;
    bottom: 60px;
    background: linear-gradient(90deg, var(--noodle-mid) 0%, var(--noodle-light) 20%, var(--noodle-mid) 45%, var(--noodle-light) 70%, var(--noodle-mid) 100%);
    opacity: 0.85;
  }
  .paper-veil {
    position: absolute;
    inset: 0;
    background: linear-gradient(180deg, var(--paper) 0%, rgba(243,244,246,0) 16%, rgba(243,244,246,0) 80%, var(--paper) 100%);
  }
  .snow-crystal {
    position: absolute;
    border-radius: 50%;
    background: radial-gradient(circle, var(--frost) 0%, rgba(255,255,255,0.4) 55%, rgba(255,255,255,0) 72%);
  }
  .snow-crystal--top { left: 250px; top: -30px; width: 220px; height: 220px; }
  .snow-crystal--left { left: 0; top: 170px; width: 140px; height: 140px; }
  .snow-crystal--right { left: 270px; top: 520px; width: 150px; height: 150px; }
  .ripples {
    position: absolute;
    left: 0;
    right: 0;
    bottom: 40px;
    height: 380px;
    background:
      radial-gradient(circle at 85% 68%, var(--ripple-deep) 0%, var(--ripple-mid) 22%, rgba(109,143,214,0) 40%),
      radial-gradient(circle at 28% 40%, var(--ripple-mid) 0%, var(--ripple-pale) 22%, rgba(201,214,240,0) 38%),
      radial-gradient(circle at 12% 90%, var(--ripple-pale) 0%, rgba(201,214,240,0) 30%);
  }
  .title {
    position: absolute;
    writing-mode: vertical-rl;
    font-family: "Yuji Syuku", serif;
    font-weight: 400;
    color: var(--ink-navy);
    font-size: 62px;
    letter-spacing: 10px;
    line-height: 1;
    margin: 0;
  }
  .title__place { left: 175px; top: 150px; }
  .title__product { left: 100px; top: 250px; }
  .description {
    position: absolute;
    left: 250px;
    top: 470px;
    width: 130px;
    height: 230px;
    writing-mode: vertical-rl;
    font-family: "Shippori Mincho", serif;
    font-weight: 500;
    font-size: 12.5px;
    line-height: 21px;
    color: var(--ink-navy);
    margin: 0;
  }
</style>
</head>
<body>
<div class="canvas">
  <div class="package">
    <div class="noodle-window" role="img" aria-label="透けて見える白い素麺の束"></div>
    <div class="paper-veil"></div>
    <div class="snow-crystal snow-crystal--top" role="img" aria-label="雪の結晶の飾り"></div>
    <div class="snow-crystal snow-crystal--left" role="img" aria-label="雪の結晶の飾り"></div>
    <div class="snow-crystal snow-crystal--right" role="img" aria-label="雪の結晶の飾り"></div>
    <div class="ripples" role="img" aria-label="青い波紋の模様"></div>
    <h1 class="title title__place">青葉台の</h1>
    <p class="title title__product">白糸そうめん</p>
    <p class="description">・使用する原材料は小麦粉・塩・水のみ。厳選した国産小麦粉をたっぷりの水で捏ね、みずみずしい透明感とツヤのある麺に仕上げました。・麺の太さは、細すぎず、適度な噛みごたえ、食べ応えが楽しめます。</p>
  </div>
</div>
</body>
</html>
```